Modern home page design for a Dental Surgery

- This design will have a 5 day deadline only.

- The design must be based around the attached HPID (home page information design) called LUMA HPID. I've attached Word and PDF versions - these are the same. The table boxes are just for approximate placement of information – you DON'T have to make it look exactly like this. All fonts used in the HPID are only examples - you can use any Google font you wish.

- Information only is in orange text. Copy to go on the design in black text. Some instructions are in the HPID. Please be creative!

- The design needs to be modern. Colours are to be black and white with grey and blue like the logo colours. Background white please.

- I've provided the images for the galleries - they are labelled and will match the name in the HPID.

- I've provided icons for the items below the gallery - the name of the image will match the subheading for each section. You can use other icons if you want to.

- This is a website that is an example of what we like. Please DON'T copy this exactly though!
http://brightmolarclinic.example.co.nz/

Width of content will be 1100 pixels when implemented as a web page. Header height (without nav bar) 150-160 pixels.

If your design is chosen the winning PSD file will have to be provided as follows…
1. Canvas size of 2000px x 2000px - 72ppi in Adobe Photoshop (CS5 compatible)
2. Width of content section is 1100px wide - centered in the canvas
3. Any button rollovers/hovers in the PSD as hidden layers.
4. All fonts used must be Google fonts (except for the fonts in the header at the top of the page).
5. You will need to supply the chosen home page plus one example page (example page as a style guide for how all other pages will look). Example page is only the header and navigational bar at the top, an empty sector in the middle with a column (180 px wide) which can be left or right aligned which means the main sector is 920 pixels wide, and then the footer at the bottom of the page

Hi Designers, The 1st posted deadline for this project was incorrect; please note new deadline for November 22.

Target Market(s)

all ages that need dental care

Industry/Entity Type

Dental

Number of Pages Required

1 page

Font styles to use
Sans Serif

Requirements
Must have
• modern clean design - as per the Project Description
Should not have
• should not be cluttered. Just because I use tables to show information placement on the HPID - you do NOT have to use boxes around information in the design.

```html
<!DOCTYPE html>
<html lang="en">
<head>
<meta charset="utf-8">
<title>Luma Dental – Home</title>
<link rel="stylesheet" href="https://fonts.googleapis.com/css2?family=Lato:wght@400;700&display=swap">
<style>
:root{
  --blue:#0e4a80;
  --blue-dark:#0a3d6b;
  --blue-bar:#0b3a66;
  --yellow:#f5ea14;
  --grey:#7a7a7a;
  --grey-light:#c9c9c9;
  --text:#2a2a2a;
  --white:#ffffff;
}
*{box-sizing:border-box;margin:0;padding:0}
html,body{width:1200px;height:2299px;overflow:hidden;background:var(--white);font-family:'Lato',Arial,sans-serif;color:var(--text)}
.page{position:relative;width:1200px;height:2299px}
.abs{position:absolute}

/* header */
.brand{left:96px;top:14px;width:170px;height:124px;text-align:center}
.brand-name{display:flex;align-items:center;justify-content:center;gap:8px;margin-top:40px;font-size:24px;font-weight:700;color:var(--blue);white-space:nowrap}
.brand-name span.dot{width:12px;height:12px;border-radius:50%;background:var(--blue);flex:none}
.brand-loc{font-size:15px;font-weight:700;color:#333;margin-top:30px;letter-spacing:1px}
.practice{left:478px;top:34px;width:200px;text-align:center;font-size:19px;line-height:24px;color:#555}
.practice strong{display:block;color:var(--blue);letter-spacing:1px;font-size:18px}
.phone{right:100px;top:52px;display:flex;align-items:center;gap:18px;font-size:25px;color:var(--blue)}
.phone small{font-size:18px;color:#666}

/* nav */
.nav{left:0;top:150px;width:1200px;height:54px;background:var(--blue)}
.nav ul{position:absolute;left:101px;display:flex;list-style:none;height:54px}
.nav li{height:54px;display:flex;align-items:center;justify-content:center;color:var(--white);font-size:15px;font-weight:700;border-right:1px solid #2b6499}
.nav li:last-child{border-right:0}
.nav li.active{background:var(--yellow);color:var(--blue-dark)}

/* hero */
.hero{left:0;top:204px;width:1200px;height:556px;background:linear-gradient(180deg,#e7ecf0 0%,#d9dde2 45%,#c8ccd1 100%)}
.hero-arrow{top:440px;width:38px;height:38px;border-radius:50%;background:rgba(255,255,255,.9);display:flex;align-items:center;justify-content:center}
.hero-card{left:89px;top:461px;width:457px;height:216px;background:rgba(255,255,255,.75);padding:24px 32px}
.hero-card h1{font-size:31px;font-weight:700;color:var(--blue);letter-spacing:.5px}
.hero-card p{font-size:18px;line-height:25px;color:#222;margin-top:8px}
.btn{display:flex;align-items:center;justify-content:center;font-size:15px;font-weight:700}
.btn-read{left:123px;top:613px;width:179px;height:34px;background:var(--blue);color:var(--white)}
.btn-gallery{left:319px;top:613px;width:179px;height:34px;border:2px solid #333;color:#222;background:rgba(255,255,255,.6)}
.dots{left:576px;top:771px;display:flex;gap:11px}
.dots i{width:8px;height:8px;border-radius:50%;background:var(--grey-light)}
.dots i:first-child{background:var(--blue)}

/* features */
.icon-circle{width:92px;height:92px;border-radius:50%;background:var(--white);box-shadow:0 2px 8px rgba(0,0,0,.18);display:flex;align-items:center;justify-content:center}
.feature{text-align:center;width:380px}
.feature h2{font-size:18px;font-weight:400;color:#222;margin-top:16px}
.feature p{font-size:13px;line-height:19px;color:#333;margin-top:6px}
.tag{height:25px;font-size:13px;color:var(--white);display:flex;align-items:center;justify-content:center}
.tag-blue{background:var(--blue)}
.tag-grey{background:var(--grey)}
.divider{left:600px;top:828px;width:1px;height:180px;background:#ccc}
.mini h3{font-size:18px;font-weight:400;color:#222}
.mini p{font-size:13px;line-height:18px;color:#333;margin-top:8px;width:210px}

/* emergency */
.emergency{left:101px;top:1359px;width:1002px;height:161px;background:var(--blue);box-shadow:4px 4px 0 #0a3259;text-align:center;color:var(--white)}
.emergency h2{font-size:18px;font-weight:400;margin-top:18px;letter-spacing:.5px}
.emergency p{font-size:15px;line-height:21px;margin:10px auto 0;width:800px}
.btn-contact{left:418px;top:1470px;width:172px;height:30px;background:var(--yellow);color:#222;font-weight:400}
.btn-call{left:608px;top:1470px;width:174px;height:30px;border:1px solid var(--white);color:var(--white);font-weight:400}

/* associations */
.assoc{left:101px;top:1588px;width:998px;height:161px;border:2px solid #ddd}
.assoc h2{position:absolute;left:196px;top:63px;font-size:25px;font-weight:400;color:#222}
.badge-a{position:absolute;left:444px;top:46px;width:108px;height:68px;border-radius:50%;background:#0d6e6e}
.badge-b{position:absolute;left:620px;top:54px;width:90px;height:52px;background:#f1d9d9}

/* footer */
.footer{left:0;top:1838px;width:1200px;height:409px;background:var(--blue)}
.fcol{position:absolute;top:50px;list-style:none;color:var(--white);font-size:13px;line-height:22.4px}
.fcol li{position:relative;padding-left:20px}
.fcol li::before{content:"";position:absolute;left:0;top:8px;width:6px;height:6px;border-radius:50%;background:#c6d3e0}
.fcol li.sub{padding-left:48px}
.fcol li.sub::before{content:">";background:none;left:28px;top:0;width:auto;height:auto;color:var(--white)}
.fcol li.sub2{padding-left:68px}
.fcol li.sub2::before{content:">";background:none;left:48px;top:0;width:auto;height:auto;color:var(--white)}
.fcol li.gap{margin-top:12px}
.fdiv{position:absolute;top:40px;width:1px;height:370px;background:#0a3c68}
.bottombar{left:0;top:2247px;width:1200px;height:52px;background:var(--blue-bar);color:var(--white);font-size:13px}
.bottombar p{position:absolute;left:98px;top:17px}
.social{position:absolute;left:1012px;top:20px;display:flex;gap:12px}
.social i{width:11px;height:11px;border-radius:50%;background:var(--white)}
</style>
</head>
<body>
<div class="page">

  <header>
    <div class="abs brand">
      <div class="brand-name"><span class="dot"></span>LUMA Group</div>
      <div class="brand-loc">TAWA</div>
    </div>
    <div class="abs practice">Northgate<br>Family Dentistry<strong>JOHNSONVILLE</strong></div>
    <div class="abs phone"><span><small>PH: </small>04 555 0142</span>
      <svg width="40" height="40" viewBox="0 0 40 40" aria-hidden="true"><circle cx="20" cy="20" r="17" fill="none" stroke="#0e4a80" stroke-width="2.5"/><path d="M14 12c1-1 2-1 3 0l2 3c.5 1 0 2-1 2.5 1 2.5 3 4.5 5.5 5.5.5-1 1.5-1.5 2.5-1l3 2c1 1 1 2 0 3-2 2-5 2-9-1s-7-7-7-10c0-2 .5-3 1-4z" fill="#0e4a80"/></svg>
    </div>
  </header>

  <nav class="abs nav">
    <ul>
      <li class="active" style="width:104px">Home</li>
      <li style="width:95px">About</li>
      <li style="width:140px">What We Do</li>
      <li style="width:161px">Why Choose Us</li>
      <li style="width:112px">Services</li>
      <li style="width:93px">Costs</li>
      <li style="width:141px">Appointment</li>
      <li style="width:153px">Contact/Map</li>
    </ul>
  </nav>

  <section class="abs hero" role="img" aria-label="Photo of a bright dental surgery room with a blue patient chair and white cabinets"></section>
  <div class="abs hero-arrow" style="left:33px"><svg width="14" height="14" viewBox="0 0 14 14"><path d="M9 2L4 7l5 5" fill="none" stroke="#666" stroke-width="2"/></svg></div>
  <div class="abs hero-arrow" style="left:1124px"><svg width="14" height="14" viewBox="0 0 14 14"><path d="M5 2l5 5-5 5" fill="none" stroke="#666" stroke-width="2"/></svg></div>
  <div class="abs hero-card">
    <h1>LUMA DENTAL</h1>
    <p>Your local dental surgery<br>Tawa &amp; Johnsonville</p>
  </div>
  <div class="abs btn btn-read">Read More</div>
  <div class="abs btn btn-gallery">View Gallery</div>
  <div class="abs dots"><i></i><i></i><i></i></div>

  <section>
    <div class="abs feature" style="left:153px;top:789px">
      <div class="icon-circle" style="margin:0 auto" role="img" aria-label="Stethoscope and tooth icon"><svg width="40" height="48" viewBox="0 0 40 48"><path d="M12 4c-4 0-6 4-5 9l3 10c1 2 3 2 3 0l1-6h4l1 6c0 2 2 2 3 0l3-10c1-5-1-9-5-9-2 0-3 1-4 1s-2-1-4-1z" fill="#3a8fd8"/><path d="M15 30v6c0 6 12 6 12 0v-4" fill="none" stroke="#333" stroke-width="2"/><circle cx="27" cy="30" r="3" fill="none" stroke="#333" stroke-width="2"/></svg></div>
      <h2>WHAT WE DO</h2>
      <p>The Luma Dental Centre offer a wide range of dental services including diagnostics, orthodontics, dentures, oral surgery, and periodontal, root canal and cosmetic dentistry.</p>
    </div>
    <div class="abs tag tag-blue" style="left:297px;top:1016px;width:92px">MORE</div>

    <div class="abs divider"></div>

    <div class="abs feature" style="left:666px;top:789px">
      <div class="icon-circle" style="margin:0 auto" role="img" aria-label="Tooth with tick icon"><svg width="36" height="44" viewBox="0 0 36 44"><path d="M10 4c-5 0-8 5-6 11l4 20c1 4 4 4 5 0l2-9h6l2 9c1 4 4 4 5 0l4-20c2-6-1-11-6-11-3 0-5 2-8 2s-5-2-8-2z" fill="none" stroke="#222" stroke-width="2"/><path d="M11 15l5 5 9-10" fill="none" stroke="#3a8fd8" stroke-width="3"/></svg></div>
      <h2>HOW MUCH DOES IT COST?</h2>
      <p>The Luma Dental Centre offer a wide range of dental services including diagnostics, orthodontics, dentures, oral surgery, and periodontal, root canal and cosmetic dentistry.</p>
    </div>
    <div class="abs tag tag-grey" style="left:815px;top:1016px;width:92px">COSTS</div>
  </section>

  <section>
    <div class="abs icon-circle" style="left:90px;top:1114px" role="img" aria-label="Dental chair icon"><svg width="44" height="40" viewBox="0 0 44 40"><path d="M6 30h30M10 30l4-14h10l6 8h8" fill="none" stroke="#3a8fd8" stroke-width="3"/><circle cx="28" cy="8" r="4" fill="#0e4a80"/></svg></div>
    <div class="abs mini" style="left:193px;top:1118px"><h3>MAKE AN APPOINTMENT</h3><p>Two convenient locations in Tawa and Johnsonville offer dental services for all ages. Take a moment to book your appoint­ment</p></div>
    <div class="abs tag tag-grey" style="left:241px;top:1258px;width:157px">APPOINTMENT</div>

    <div class="abs icon-circle" style="left:431px;top:1114px" role="img" aria-label="Sparkling tooth icon"><svg width="36" height="44" viewBox="0 0 36 44"><path d="M10 6c-5 0-8 5-6 11l4 20c1 4 4 4 5 0l2-9h6l2 9c1 4 4 4 5 0l4-20c2-6-1-11-6-11-3 0-5 2-8 2s-5-2-8-2z" fill="none" stroke="#222" stroke-width="2"/><path d="M30 1v8M26 5h8" stroke="#3a8fd8" stroke-width="2"/></svg></div>
    <div class="abs mini" style="left:535px;top:1118px"><h3>YOUR FIRST CONSULTATION</h3><p>Want to know what will happen in your first consultation? Check out our first dental consultation pro­cess.</p></div>
    <div class="abs tag tag-grey" style="left:605px;top:1258px;width:163px">FIRST CONSULTATION</div>

    <div class="abs icon-circle" style="left:789px;top:1114px" role="img" aria-label="Clipboard form icon"><svg width="34" height="42" viewBox="0 0 34 42"><rect x="3" y="5" width="28" height="35" rx="3" fill="none" stroke="#3a8fd8" stroke-width="3"/><rect x="11" y="2" width="12" height="6" fill="#0e4a80"/><path d="M9 18h16M9 25h16M9 32h10" stroke="#0e4a80" stroke-width="2"/></svg></div>
    <div class="abs mini" style="left:892px;top:1118px"><h3>APPLICATION FORM</h3><p>Save time and fill in an online application form (or download, print out and complete) before your first visit.</p></div>
    <div class="abs tag tag-grey" style="left:926px;top:1258px;width:165px">APPLICATION</div>
  </section>

  <section class="abs emergency">
    <h2>IS THIS AN EMERGENCY?</h2>
    <p>Lorem ipsum dolor sit amet, consectetur adipiscing elit. Aenean eget sem lobortis, aliquet neque non, placerat eros. Donec ultricies quam non dui lobortis tristique.</p>
  </section>
  <div class="abs btn btn-contact">Contact</div>
  <div class="abs btn btn-call">Call - 04 555 0142</div>

  <section class="abs assoc">
    <h2>ASSOCIATIONS :</h2>
    <div class="badge-a" role="img" aria-label="Association badge"></div>
    <div class="badge-b" role="img" aria-label="Association badge"></div>
  </section>

  <footer class="abs footer">
    <ul class="fcol" style="left:104px">
      <li>Home</li><li>About</li><li class="sub">Team</li><li class="sub">Registration form</li><li>What We Do</li><li>Why Choose Us</li><li class="sub">Testimonials</li><li>Costs</li><li>Appointment</li><li>Contact / Map</li><li>Services</li>
    </ul>
    <div class="fdiv" style="left:268px"></div>
    <ul class="fcol" style="left:291px">
      <li>Restorative Dentistry</li><li>Preventative</li><li class="sub">Fissure Sealants</li><li class="sub">Mouthguards</li><li class="sub">Bite Splints</li><li>Fillings</li><li class="sub">Amalgams, Composites (white fillings)</li><li class="sub">Porcelain &amp; Gold</li><li>Crown &amp; Bridge Treatment</li><li>Implants</li>
    </ul>
    <div class="fdiv" style="left:559px"></div>
    <ul class="fcol" style="left:582px;width:250px">
      <li>Oral Surgery</li><li class="sub">Extractions</li><li class="sub">Minor Impacted Wisdom Teeth</li>
      <li class="gap">Periodontal (gum) Care</li><li class="sub">Hygiene Services</li><li class="sub">Minor Periodontal Surgery</li><li class="sub">Preventative Services</li>
      <li class="gap">Root Canal Therapy</li>
      <li class="gap">Cosmetic</li><li class="sub">Porcelain Veneers</li><li class="sub">Glow! Bleaching (in surgery teeth whitening)</li>
      <li class="gap">Dentures</li>
    </ul>
    <div class="fdiv" style="left:837px"></div>
    <ul class="fcol" style="left:869px;width:240px">
      <li>Orthodontics</li>
      <li class="gap">Children &amp; pre-schoolers</li><li class="sub">Free Secondary School Dentistry</li><li class="sub2">Free Dental Care Under 18</li><li class="sub">Pre-school Dentistry</li>
      <li class="gap">Oral Care Products</li>
      <li class="gap">Diagnostic Dentistry</li><li class="sub">Digital X-rays</li><li class="sub">Panoramic X-rays</li><li class="sub">Intra-oral photography &amp; Camera</li><li class="sub">Laser Cavity Detection</li>
    </ul>
  </footer>
  <div class="abs bottombar">
    <p>Copyrights © 2014 yoursite, All rights reserved</p>
    <div class="social"><i></i><i></i><i></i><i></i></div>
  </div>

</div>
</body>
</html>
```